Structural Engineering Firm Looking for High-Impact Lead Generation Focused Design (for B2B)

A well-established structural engineering firm in the UK wants a new website designed for them which will help them realise more business from online. Directly through the website as well as Ads and lead platforms. They need to compare favourably to competitors and have clarity. Current Site is here: http://www.marlowgrantpartners.example/ - you can take imagery from this site if you want to help with the design.
Updates

Target Market(s)

Homeowners, Architects, Designers, Construction Companies and Landlords

Industry/Entity Type

Professional Services

Number of Pages Required

5+ page

Font styles to use
Sans Serif

Requirements
Must have
• A Strong, Simple and Professional Design with a Focus on Lead Generation
Nice to have
• Creativity in the Detail, Clear Messaging
Should not have
• Too Much Colour, Too 'Consumer', Too Much Variation

```html
<!DOCTYPE html>
<html lang="en">
<head>
<meta charset="utf-8">
<title>Marlow Grant Partners – Structural Engineers</title>
<link href="https://fonts.googleapis.com/css2?family=Montserrat:wght@400;500;600;700&display=swap" rel="stylesheet">
<style>
:root{
  --bg:#262626;
  --panel:#2c2c2c;
  --card:#383838;
  --accent:#f2d21b;
  --text:#ffffff;
  --muted:#bdbdbd;
  --hero:#6f7477;
}
*{margin:0;padding:0;box-sizing:border-box}
html,body{width:680px;height:1200px;overflow:hidden;background:var(--bg)}
body{position:relative;font-family:'Montserrat',sans-serif;color:var(--text)}
.abs{position:absolute}
.intro-text{left:0;top:0;width:310px;font-size:10px;line-height:13px;color:var(--muted)}
.top-photo-strip{left:360px;top:0;width:160px;height:6px;background:#8a8f93}
.service-label{font-weight:700;font-size:19px;color:var(--accent)}
.service-label .white{color:var(--text)}
.designers-label{left:522px;top:16px}
.contractors-photo{left:188px;top:66px;width:156px;height:106px;background:linear-gradient(180deg,#9aa0a6,#4a4f55)}
.contractors-label{left:0;width:680px;text-align:center;top:184px}
.hero{left:0;top:236px;width:680px;height:374px;background:linear-gradient(180deg,#8b9093 0%,#5e6366 60%,#4d5154 100%)}
.hero-title{left:0;width:680px;top:308px;text-align:center;font-weight:600;font-size:19px}
.hero-copy{left:60px;width:560px;top:392px;text-align:center;font-size:12.5px;line-height:34px;color:#f1f1f1}
.arrow{top:414px}
.arrow-left{left:20px}
.arrow-right{right:20px}
.dots{left:282px;top:564px;display:flex;gap:20px}
.dot{width:12px;height:12px;border-radius:50%;background:var(--accent)}
.dot.off{background:var(--text)}
.clients{left:0;top:610px;width:680px;height:280px;background:var(--panel)}
.clients-title{left:0;width:680px;top:664px;text-align:center;font-weight:700;font-size:19px;color:var(--accent)}
.card{top:764px;width:294px;height:116px;background:var(--card)}
.card-a{left:36px}.card-b{left:350px}
.avatar{top:738px;width:56px;height:56px;border-radius:50%}
.avatar-a{left:42px;background:#e69a2b}
.avatar-b{left:354px;background:#f3f3f3}
.card-dots{top:774px;font-size:16px;color:var(--accent);letter-spacing:4px}
.card-dots-a{left:288px}.card-dots-b{left:592px}
.card-text{top:806px;width:270px;text-align:center;font-size:9.5px;line-height:12px;color:var(--muted)}
.card-text-a{left:48px}.card-text-b{left:362px}
.map{left:36px;top:945px;width:297px;height:146px;background:linear-gradient(135deg,#e9ebe6,#cfd6d0)}
.contact{left:358px;top:945px}
.contact h3{font-size:13px;font-weight:700;margin-bottom:8px}
.contact p{font-size:10px;line-height:19px;color:#e5e5e5}
.contact .c{text-align:center;width:108px}
.divider{left:460px;top:945px}
.address{left:462px;top:1000px;width:212px;text-align:center}
.address h3{font-size:13px;font-weight:700;margin-bottom:6px;margin-left:24px}
.address p{font-size:9.5px;line-height:19px;color:#e5e5e5}
.footer-rule{left:0;top:1118px;width:680px;height:1px;background:#3a3a3a}
.footer-links{top:1143px;font-size:10px;color:#e5e5e5}
.terms{left:190px}.privacy{left:432px}
.copyright{left:0;width:680px;top:1163px;text-align:center;font-size:6px;color:#8a8a8a}
</style>
</head>
<body>
<p class="abs intro-text">neighbour's property? If you are then it is highly likely the works fall under the Party Wall Etc. Act 1996. The Act dictates what a property owner, whether residential or commercial, must do before commencing works on site.</p>
<div class="abs top-photo-strip" role="img" aria-label="Photo of a completed design project"></div>
<h2 class="abs service-label designers-label"><span class="white">Desig</span>ners</h2>
<div class="abs contractors-photo" role="img" aria-label="Photo of a modern terraced building facade"></div>
<h2 class="abs service-label contractors-label">Contractors</h2>

<section class="abs hero" role="img" aria-label="Photo of a bright open-plan kitchen and dining interior"></section>
<h1 class="abs hero-title">PARTY WALL ETC ACT 1996</h1>
<p class="abs hero-copy">Are you planning an extension or alterations that could affect your neighbour's property? If you are then it is highly likely the works fall under the Party Wall etc. Act 1996. The Act dictates what a property owner, whether residential or commercial, must do before commencing works on site.</p>
<svg class="abs arrow arrow-left" width="46" height="20" viewBox="0 0 46 20"><path d="M44 10H4M12 2L3 10l9 8" fill="none" stroke="#fff" stroke-width="2.5"/></svg>
<svg class="abs arrow arrow-right" width="46" height="20" viewBox="0 0 46 20"><path d="M2 10h40M34 2l9 8-9 8" fill="none" stroke="#fff" stroke-width="2.5"/></svg>
<div class="abs dots"><span class="dot"></span><span class="dot"></span><span class="dot"></span><span class="dot off"></span></div>

<section class="abs clients"></section>
<h2 class="abs clients-title">From Our Great Clients</h2>
<div class="abs card card-a"></div>
<div class="abs card card-b"></div>
<div class="abs avatar avatar-a" role="img" aria-label="Client avatar illustration"></div>
<div class="abs avatar avatar-b" role="img" aria-label="Client avatar illustration"></div>
<span class="abs card-dots card-dots-a">••</span>
<span class="abs card-dots card-dots-b">••</span>
<p class="abs card-text card-text-a">Lorem ipsum dolor sit amet, consectetur adipiscing elit, sed do eiusmod tempor incididunt ut labore. Lorem ipsum dolor sit amet, consectetur adipiscing elit, sed do eiusmod tempor incididunt ut labore</p>
<p class="abs card-text card-text-b">Lorem ipsum dolor sit amet, consectetur adipiscing elit, sed do eiusmod tempor incididunt ut labore. Lorem ipsum dolor sit amet, consectetur adipiscing elit, sed do eiusmod tempor incididunt ut labore</p>

<div class="abs map" role="img" aria-label="Street map showing the office location"></div>
<div class="abs contact">
  <h3>GET IN TOUCH</h3>
  <p class="c">+44 (0) 20 7946 0815</p>
  <p class="c">+44 (0) 1632 960 442</p>
  <p>info@marlowgrantpartners.example</p>
</div>
<svg class="abs divider" width="60" height="146" viewBox="0 0 60 146"><line x1="56" y1="2" x2="6" y2="144" stroke="var(--accent)" stroke-width="2"/></svg>
<div class="abs address">
  <h3>SITE ADDRESS</h3>
  <p>Studio 4 Harbour Works</p>
  <p>12 Calder Lane</p>
  <p>London SE9 4QT</p>
  <p>(Our Kent Office is Westbrook, Kent)</p>
</div>

<div class="abs footer-rule"></div>
<a class="abs footer-links terms">Terms &amp; Conditions</a>
<a class="abs footer-links privacy">Privacy Policy</a>
<p class="abs copyright">Copyright 2018. All rights reserved.</p>
</body>
</html>
```